Saucy Velvet Kittenz Business Card

We need business cards designed for our consultants to use and hand out to customers.
We are an Adult party plan company (like Crispaboxa but sex toys and lingerie)
We would like bright colours pinks, purples.
The cards need our logo
Space for the reps phone number email address and name.
We need our website on it www.saucyvelvetkittens.com.au

```html
<!DOCTYPE html>
<html lang="en">
<head>
<meta charset="utf-8">
<title>Saucy Velvet Kittenz – Business Card</title>
<link href="https://fonts.googleapis.com/css2?family=Open+Sans:wght@400;600&display=swap" rel="stylesheet">
<style>
  :root {
    --backdrop: #3b3b3d;
    --magenta-light: #dc3d8f;
    --magenta-dark: #c8166f;
    --logo-on-pink: #f59ccb;
    --pink: #ee3d96;
    --paper: #f1f1f1;
    --ink: #333338;
    --stitch: #d4d4d4;
  }
  * { margin: 0; padding: 0; box-sizing: border-box; }
  html, body {
    width: 1200px; height: 819px; overflow: hidden;
    background: var(--backdrop);
    font-family: "Open Sans", Arial, sans-serif;
  }
  .stage { position: relative; width: 1200px; height: 819px; }

  .card {
    position: absolute; top: 250px;
    width: 520px; height: 318px;
    border-radius: 6px;
    box-shadow: 0 14px 30px rgba(0,0,0,.45);
  }
  .card--front {
    left: 50px;
    background: linear-gradient(160deg, var(--magenta-light) 0%, var(--magenta-dark) 100%);
  }
  .card--back {
    left: 630px;
    background: var(--paper);
  }
  .card__frame {
    position: absolute; inset: 8px;
    border: 1.5px dashed var(--stitch);
    border-radius: 3px;
  }

  .brand {
    position: absolute;
    display: flex; align-items: center; gap: 10px;
    font-weight: 600; white-space: nowrap;
  }
  .brand__dot { width: 16px; height: 16px; border-radius: 50%; }
  .card--front .brand { left: 40px; top: 136px; font-size: 28px; color: var(--logo-on-pink); }
  .card--front .brand__dot { background: var(--logo-on-pink); }
  .card--back .brand { left: 36px; top: 38px; font-size: 24px; color: var(--pink); }
  .card--back .brand__dot { background: var(--pink); width: 14px; height: 14px; }

  .rep {
    position: absolute; right: 34px; bottom: 30px;
    text-align: right;
  }
  .rep__name {
    color: var(--pink); font-size: 26px; font-weight: 400;
    letter-spacing: 2px; margin-bottom: 8px;
  }
  .rep__line {
    display: flex; justify-content: flex-end; align-items: center; gap: 8px;
    color: var(--ink); font-size: 15px; line-height: 21px; letter-spacing: .5px;
  }
  .rep__line svg { width: 13px; height: 13px; fill: var(--pink); flex: none; }
</style>
</head>
<body>
<main class="stage">
  <section class="card card--front">
    <div class="brand"><span class="brand__dot"></span>Saucy Velvet Kittenz</div>
  </section>

  <section class="card card--back">
    <div class="card__frame"></div>
    <div class="brand"><span class="brand__dot"></span>Saucy Velvet Kittenz</div>
    <div class="rep">
      <p class="rep__name">Your Name</p>
      <p class="rep__line">0400 517 283
        <svg viewBox="0 0 16 16"><path d="M4 0h8a1.5 1.5 0 0 1 1.5 1.5v13A1.5 1.5 0 0 1 12 16H4a1.5 1.5 0 0 1-1.5-1.5v-13A1.5 1.5 0 0 1 4 0zm0 2v10.5h8V2zm4 11.3a.9.9 0 1 0 0 1.8.9.9 0 0 0 0-1.8z"/></svg>
      </p>
      <p class="rep__line">info@saucyvelvetkittens.com.au
        <svg viewBox="0 0 16 16"><path d="M0 3h16v1.2L8 9 0 4.2zm0 2.6 8 4.8 8-4.8V13H0z"/></svg>
      </p>
      <p class="rep__line">www.saucyvelvetkittens.com.au
        <svg viewBox="0 0 16 16"><path d="M8 1 0 8h2.2v7h4.3v-4.5h3V15h4.3V8H16z"/></svg>
      </p>
    </div>
  </section>
</main>
</body>
</html>
```